Marrowfield Benefit Advisors Business Card Design

I already placed order for cards through sketch hive.

Double sided- back Navy with White logo and raised silver "swoosh"

```html
<!DOCTYPE html>
<html lang="en">
<head>
<meta charset="utf-8">
<title>Marrowfield Benefit Advisors – Business Card</title>
<link href="https://fonts.googleapis.com/css2?family=Open+Sans:wght@400;600;700&display=swap" rel="stylesheet">
<style>
  :root {
    --navy: #14275a;
    --navy-deep: #0f1f4a;
    --navy-tone: #1d3576;
    --white: #ffffff;
    --silver: #c9ced8;
    --stage: #2b2e33;
  }
  * { box-sizing: border-box; margin: 0; padding: 0; }
  html, body { width: 1200px; height: 900px; overflow: hidden; }
  body {
    background: var(--stage);
    font-family: "Open Sans", Arial, sans-serif;
    position: relative;
  }
  .card {
    position: absolute;
    top: 300px;
    width: 520px;
    height: 300px;
    overflow: hidden;
    box-shadow: 0 12px 30px rgba(0,0,0,.45);
  }
  .card-front { left: 60px; background: var(--white); }
  .card-back { left: 620px; background: var(--navy); }

  .front-brand {
    height: 150px;
    display: flex;
    align-items: center;
    justify-content: center;
    gap: 14px;
  }
  .brand-dot {
    width: 18px; height: 18px; border-radius: 50%;
    background: var(--navy);
  }
  .brand-name {
    color: var(--navy);
    font-weight: 600;
    font-size: 24px;
    letter-spacing: .5px;
  }
  .front-details {
    height: 150px;
    background: var(--navy);
    display: flex;
    align-items: center;
    padding: 0 34px;
    color: var(--white);
  }
  .person { text-align: right; padding-right: 22px; }
  .person-name { font-weight: 700; font-size: 22px; }
  .person-role { font-size: 13px; color: var(--silver); margin-top: 2px; }
  .divider { width: 1px; height: 74px; background: var(--silver); opacity: .7; }
  .contacts { list-style: none; padding-left: 22px; font-size: 14px; }
  .contacts li { display: flex; align-items: center; gap: 10px; line-height: 26px; }
  .contacts svg { width: 14px; height: 14px; fill: var(--white); flex: none; }

  .back-field {
    position: absolute; inset: 0;
    background: linear-gradient(135deg, var(--navy-tone) 0%, var(--navy) 45%, var(--navy-deep) 100%);
  }
  .back-brand {
    position: absolute; inset: 0;
    display: flex; align-items: center; justify-content: center; gap: 12px;
    padding-top: 80px;
  }
  .back-brand .brand-dot { background: var(--silver); }
  .back-brand .brand-name { color: var(--white); font-size: 26px; }
</style>
</head>
<body>
  <section class="card card-front">
    <div class="front-brand">
      <span class="brand-dot"></span>
      <span class="brand-name">Marrowfield Benefit Advisors</span>
    </div>
    <div class="front-details">
      <div class="person">
        <div class="person-name">Owen Tallis</div>
        <div class="person-role">Owner</div>
      </div>
      <div class="divider"></div>
      <ul class="contacts">
        <li>
          <svg viewBox="0 0 24 24"><path d="M6.6 10.8a15.1 15.1 0 0 0 6.6 6.6l2.2-2.2a1 1 0 0 1 1-.25 11.4 11.4 0 0 0 3.6.57 1 1 0 0 1 1 1V20a1 1 0 0 1-1 1A17 17 0 0 1 3 4a1 1 0 0 1 1-1h3.5a1 1 0 0 1 1 1c0 1.25.2 2.45.57 3.6a1 1 0 0 1-.25 1z"/></svg>
          (555)014-2871
        </li>
        <li>
          <svg viewBox="0 0 24 24"><path d="M2 5h20v14H2z M2 5l10 8 10-8" fill="none" stroke="#fff" stroke-width="2"/></svg>
          info@marrowfield.com
        </li>
        <li>
          <svg viewBox="0 0 24 24"><circle cx="12" cy="12" r="9" fill="none" stroke="#fff" stroke-width="2"/><path d="M3 12h18M12 3c3 3 3 15 0 18M12 3c-3 3-3 15 0 18" fill="none" stroke="#fff" stroke-width="1.6"/></svg>
          info@marrowfield.com
        </li>
      </ul>
    </div>
  </section>

  <section class="card card-back">
    <div class="back-field" role="img" aria-label="Tone-on-tone repeating brand monogram pattern in navy blues"></div>
    <div class="back-brand">
      <span class="brand-dot"></span>
      <span class="brand-name">Marrowfield</span>
    </div>
  </section>
</body>
</html>
```